Wattlebrook Property Maintenance needs a logo and business card

Maintenance company providing Residential/Commercial small building and maintenance works.This start up company needs a professional image with a new logo/business card.

The company name is 'Wattlebrook Property Maintenance'

The logo/business card should use the colour ORANGE.

Would like solid colour orange with logo on one side.
Name and business details on the other.

I would like a picture of a 'house' as part of the logo.

Need to be professional and classy but with a slightly softer edge to appeal to female as well as male clients.

The text on the card and tag line for the business to be included on the card as follows:

"Wattlebrook Property Maintenance
Careful, reliable work for every home and office ..."

Declan Hayes

(Icons for Ph. Email. Mob. and Web address)

MOB. 0491 570 156
PH. 03 5550 1234
Email: declan@wattlebrookpropertymaintenance.com.au
Address: 47 Fenwick Street, Ashbury Vale VIC 3999
Web: wattlebrookpropertymaintenance.com.au

Target Market(s)

35 to 55 year old time poor professional white collar

Industry/Entity Type

Building

Logo Text

Wattlebrook Property Maintenance (tag line: A Commitment to Quality and Exceptional Service)

Font styles to use
Sans Serif

Requirements
Must have
• The logo picture should be of a house
Should not have
• Do not want references to orange 'fruit' in the design

```html
<!DOCTYPE html>
<html lang="en">
<head>
<meta charset="utf-8">
<title>Wattlebrook Property Maintenance – Business Card</title>
<link rel="stylesheet" href="https://fonts.googleapis.com/css2?family=Arimo:wght@400;700&display=swap">
<style>
  :root {
    --orange: #f47a0f;
    --peach: #fde3cc;
    --grey: #7a7a7a;
    --white: #ffffff;
    --backdrop: #e4e4e4;
  }
  html, body {
    margin: 0;
    padding: 0;
    width: 1200px;
    height: 844px;
    overflow: hidden;
    background: var(--backdrop);
    font-family: "Arimo", Arial, sans-serif;
  }
  .canvas {
    position: relative;
    width: 1200px;
    height: 844px;
  }
  .card {
    position: absolute;
    left: 258px;
    width: 684px;
    height: 375px;
    overflow: hidden;
  }
  .card-front { top: 28px; background: var(--white); }
  .card-back { top: 442px; background: var(--orange); color: var(--white); }

  .corner {
    position: absolute;
    width: 120px;
    height: 120px;
  }
  .corner-top-left { left: 0; top: 0; }
  .corner-bottom-right { right: 0; bottom: 0; transform: rotate(180deg); }

  .soft-circle {
    position: absolute;
    left: 345px;
    top: -110px;
    width: 420px;
    height: 420px;
    border-radius: 50%;
    background: var(--peach);
  }

  .brand-square {
    position: absolute;
    left: 92px;
    top: 140px;
    width: 64px;
    height: 64px;
    background: var(--orange);
  }
  .brand {
    position: absolute;
  }
  .brand-front { left: 186px; top: 132px; }
  .brand-back { left: 0; width: 100%; top: 140px; text-align: center; }

  .brand-name {
    margin: 0;
    font-weight: 700;
    font-size: 30px;
    line-height: 1.15;
    color: var(--orange);
  }
  .brand-back .brand-name {
    font-size: 38px;
    color: var(--white);
  }
  .tagline {
    margin: 10px 0 0;
    font-size: 13px;
    font-weight: 400;
    color: var(--grey);
  }
  .brand-back .tagline {
    font-size: 15px;
    color: var(--white);
  }

  .person-name {
    position: absolute;
    top: 24px;
    left: 0;
    width: 100%;
    text-align: center;
    font-size: 22px;
    font-weight: 400;
    text-transform: uppercase;
    margin: 0;
  }
  .person-name strong { font-weight: 700; }

  .contact-list {
    position: absolute;
    left: 16px;
    top: 262px;
    margin: 0;
    padding: 0;
    list-style: none;
    font-size: 11.5px;
    line-height: 19px;
    text-transform: uppercase;
    letter-spacing: 0.2px;
  }
</style>
</head>
<body>
<main class="canvas">

  <section class="card card-front" aria-label="Card front">
    <div class="soft-circle"></div>
    <svg class="corner corner-top-left" viewBox="0 0 120 120" aria-hidden="true">
      <polygon points="0,0 62,0 0,62" fill="var(--orange)" opacity="0.35"/>
      <polygon points="0,0 48,0 0,48" fill="var(--orange)" opacity="0.6"/>
      <polygon points="0,0 36,0 0,36" fill="var(--orange)"/>
    </svg>
    <svg class="corner corner-bottom-right" viewBox="0 0 120 120" aria-hidden="true">
      <polygon points="0,0 120,0 0,120" fill="var(--orange)" opacity="0.3"/>
      <polygon points="0,0 100,0 0,100" fill="var(--orange)" opacity="0.55"/>
      <polygon points="0,0 80,0 0,80" fill="var(--orange)"/>
    </svg>
    <div class="brand-square" aria-hidden="true"></div>
    <div class="brand brand-front">
      <p class="brand-name">Wattlebrook Property<br>Maintenance</p>
      <p class="tagline">Careful, reliable work for every home and office ...</p>
    </div>
  </section>

  <section class="card card-back" aria-label="Card back">
    <svg class="corner corner-top-left" viewBox="0 0 120 120" aria-hidden="true">
      <polygon points="0,0 70,0 0,70" fill="var(--white)" opacity="0.3"/>
      <polygon points="0,0 55,0 0,55" fill="var(--white)" opacity="0.55"/>
      <polygon points="0,0 40,0 0,40" fill="var(--white)" opacity="0.85"/>
    </svg>
    <svg class="corner corner-bottom-right" viewBox="0 0 120 120" aria-hidden="true">
      <polygon points="0,0 40,0 0,40" fill="var(--white)" opacity="0.5"/>
      <polygon points="0,0 26,0 0,26" fill="var(--white)" opacity="0.85"/>
    </svg>
    <h1 class="person-name">Declan <strong>Hayes</strong></h1>
    <div class="brand brand-back">
      <p class="brand-name">Wattlebrook Property Maintenance</p>
      <p class="tagline">Careful, reliable work for every home and office ...</p>
    </div>
    <ul class="contact-list">
      <li>Mob. 0491 570 156</li>
      <li>Ph. 03 5550 1234</li>
      <li>Email: declan@wattlebrookpropertymaintenance.com.au</li>
      <li>Address: 47 Fenwick Street, Ashbury Vale VIC 3999</li>
      <li>Web: wattlebrookpropertymaintenance.com.au</li>
    </ul>
  </section>

</main>
</body>
</html>
```